letter head for a construction company

Company Name: Kaleshi Construction Limited

Address: Tumbili Street, Kigamboni Shores, Dar es salaam, Tanzania

Phone: 0754382916

email : info@kaleshiconstruction.example

website : www.kaleshiconstruction.example

```html
<!DOCTYPE html>
<html lang="en">
<head>
<meta charset="utf-8">
<title>Kaleshi Construction Limited – Letterhead</title>
<link rel="stylesheet" href="https://fonts.googleapis.com/css2?family=Arimo:wght@400&family=Montserrat:wght@600;700&display=swap">
<style>
  :root {
    --backdrop: #e2e2e2;
    --paper: #ffffff;
    --ink: #555657;
    --ink-dark: #444545;
    --band: #444545;
    --accent: #ec7a08;
    --on-band: #ffffff;
    --placeholder: #e4e4e4;
  }
  * { margin: 0; padding: 0; box-sizing: border-box; }
  html, body {
    width: 978px; height: 1200px; overflow: hidden;
    background: var(--backdrop);
  }
  .letterhead {
    position: absolute; left: 138px; top: 104px;
    width: 703px; height: 992px;
    background: var(--paper);
    overflow: hidden;
  }
  .brand {
    position: absolute; left: 59px; top: 80px;
    display: flex; align-items: center; gap: 8px;
  }
  .brand-mark {
    width: 12px; height: 12px; background: var(--accent);
  }
  .brand-name {
    font-family: "Montserrat", sans-serif; font-weight: 700;
    font-size: 15px; letter-spacing: 1.5px; color: var(--ink-dark);
  }
  .salutation {
    position: absolute; left: 64px; top: 304px;
    font-family: "Montserrat", sans-serif; font-weight: 700;
    font-size: 16px; color: var(--ink);
  }
  .letter-body {
    position: absolute; left: 63px; top: 353px; width: 580px;
    font-family: "Arimo", sans-serif; font-size: 11.8px;
    line-height: 14.4px; color: var(--ink); white-space: nowrap;
  }
  .letter-body p + p { margin-top: 12.6px; }
  .closing {
    position: absolute; left: 64px; top: 650px;
    font-family: "Montserrat", sans-serif; font-weight: 700;
    font-size: 9px; color: var(--ink);
  }
  .signature {
    position: absolute; left: 64px; top: 690px;
    width: 115px; height: 36px; background: var(--placeholder);
  }
  .footer-band {
    position: absolute; left: 0; top: 915px;
    width: 703px; height: 77px; background: var(--band);
  }
  .footer-peak { position: absolute; left: 0; top: 0; }
  .contact-list, .address {
    position: absolute; top: 11px; list-style: none;
    font-family: "Arimo", sans-serif; font-size: 11.3px;
    line-height: 13.6px; color: var(--on-band);
  }
  .contact-list { left: 36px; }
  .contact-list li { display: flex; align-items: center; gap: 6px; }
  .contact-list svg { width: 9px; height: 9px; flex: none; }
  .address { right: 36px; text-align: right; font-style: normal; }
</style>
</head>
<body>
  <main class="letterhead">
    <header class="brand">
      <span class="brand-mark"></span>
      <span class="brand-name">KALESHI CONSTRUCTION LIMITED</span>
    </header>

    <h1 class="salutation">Dear Mr. Smith,</h1>

    <section class="letter-body">
      <p>Lorem ipsum dolor sit amet, consectetuer adipiscing elit, sed diam nonmmy nibh euismod tincidunt ut laor<br>eet dolore magna aliquam erat volutpat. Ut wisi enim ad minim veniam, quis nostrud exerci tationmcorper<br>suscipit lobortis nisl ut aliquip ex ea commodo consequat. Duis autem vel eum iriure dolor in hendrerit in<br>vulputate velit esse molestie consequat, vel illum dolore eu feugiat</p>
      <p>Rorem ipsum dolor sit amet, consectetuer adipiscing elit, sed diam nonmmy nibh euismod tincidunt ut laor<br>eet dolore magna aliquam erat volutpat. Ut wisi enim ad minim veniam, quis nostrud exerci tationmcorper<br>suscipit lobortis nisl ut aliquip ex ea commodo consequat. Duis autem vel eum iriure dolor in hendrerit in<br>vulputate velit esse molest</p>
      <p>Dorem ipsum dolor sit amet, consectetuer adipiscing elit, sed diam nonmmy nibh euismod tincidunt ut laor<br>eet dolore magna aliquam erat volutpat. Ut wisi enim ad minim veniam, quis nostrud exerci tationmcorper<br>suscipit lobortis nisl ut aliquip ex ea commodo consequat. Duis autem vel eum iriure dolor in hendrerit in<br>suscipit lobortis nisl ut aliquip ex ea commodo consequat. Duis autem vel eum iriure dolor in hendrerit in<br>vulputate velit esse molestie consequat, vel illum</p>
      <p>Sorem ipsum dolor sit amet, consectetuer adipiscing elit, sed diam nonmmy nibh euismod tincidunt ut laor<br>eet dolore magna aliquam erat volutpat. Ut wisi enim ad minim veniam, quis nostrud exerci tationmcorper<br>suscipit lobortis nisl ut aliquip ex ea commodo consequat. Duis autem vel eum iriure dolor in</p>
    </section>

    <p class="closing">Sincerely,</p>
    <div class="signature" role="img" aria-label="Handwritten signature"></div>

    <footer class="footer-band">
      <svg class="footer-peak" width="703" height="77" viewBox="0 0 703 77">
        <polygon points="352,-1 410,77 292,77" fill="#ffffff"/>
        <polygon points="352,16 402,77 300,77" fill="var(--accent)"/>
      </svg>
      <ul class="contact-list">
        <li>
          <svg viewBox="0 0 10 10"><path d="M2 1 L4 1 L4.6 3.2 L3.4 4 Q4.3 5.8 6 6.6 L6.8 5.4 L9 6 L9 8 Q8.5 9 7.5 9 Q1 8.5 1 2.5 Q1 1.5 2 1 Z" fill="var(--accent)"/></svg>
          0754382916
        </li>
        <li>
          <svg viewBox="0 0 10 10"><rect x="0.5" y="2" width="9" height="6.5" fill="var(--accent)"/><path d="M0.5 2 L5 5.6 L9.5 2" fill="none" stroke="var(--band)" stroke-width="0.9"/></svg>
          info@kaleshiconstruction.example
        </li>
        <li>
          <svg viewBox="0 0 10 10"><circle cx="5" cy="5" r="4.5" fill="var(--accent)"/><path d="M0.5 5 H9.5 M5 0.5 Q2.5 5 5 9.5 M5 0.5 Q7.5 5 5 9.5" fill="none" stroke="var(--band)" stroke-width="0.7"/></svg>
          www.kaleshiconstruction.example
        </li>
      </ul>
      <address class="address">
        Tumbili Street<br>
        Kigamboni Shores<br>
        Dar es salaam, Tanzania
      </address>
    </footer>
  </main>
</body>
</html>
```